Merrow's Voyage Atlas Mobile App

We need a sleek new design for our new mobile app we are launching in the South Pacific. This app will be released for both Lumafone and Corvex. The app has already been developed and your new design will give it the finishing touch we need to release it to our audience. This will be the premiere tourism app for the South Pacific and will be advertised heavily in our successful print publications which are distributed internationally. We are looking for you to provide two designs (for two screens in our mobile app) for this competition. The selected winner will have the opportunity to design the remaining screens in our app and website as a separate contract.

Attached you will see a few of the screens that currently exist in our mobile app to give you a feel for the functionality. The two screens we want you to design for this competition are the main listing page and the category selection page. These two screens will be included in the uploaded files and will be clearly marked so you know what we are looking for.

Please feel free to reach out to us with any questions if you need any guidance in directing your designs. Show us something sleek, engaging, and ultimately something that will drive our users to want to engage with the businesses that are listed in the app.

Please see the uploaded files for a couple of our current designs, the two screens we want you to design for this competition, and a few samples of design ideas we like.

Best of Luck!

Target Market(s)

Travelers to the South Pacific

Industry/Entity Type

Travel Industry

Font styles to use
Serif
Sans Serif

Colors
0492cd
33a6d7
ec1f27
f04a50
85cae6
cee9f5
f59296
cedeed
fbd4d5

Requirements
Must have
• Clean, attractive design for the two screens mentioned in the brief.
Nice to have
• Icon sets, color guide, font selection
Should not have
• Project should not be too busy or incorporate too many different colors, styles, fonts, etc.

```html
<!DOCTYPE html>
<html lang="en">
<head>
<meta charset="utf-8">
<title>Merrow's Voyage Atlas – Categories</title>
<link rel="stylesheet" href="https://fonts.googleapis.com/css2?family=Lato:wght@300;400;700&family=Roboto:wght@500;700&display=swap">
<style>
  :root {
    --brand-blue: #2a86e6;
    --header-deep: #0f4fb4;
    --header-mid: #2a6fd0;
    --header-light: #3f8ee0;
    --white: #ffffff;
    --search-bg: #f4f4f4;
    --search-text: #9a9a9a;
    --label: #222222;
    --nav-icon: #a9a9a9;
    --divider: #e6e6e6;
    --fab-top: #dc0d4c;
    --fab-bottom: #ef4a2c;
  }
  * { box-sizing: border-box; margin: 0; padding: 0; }
  html, body { width: 675px; height: 1200px; overflow: hidden; background: var(--white); }
  .screen { position: relative; width: 675px; height: 1200px; overflow: hidden; background: var(--white); font-family: 'Roboto', sans-serif; }

  .hero {
    position: absolute; left: 0; top: 0; width: 675px; height: 406px;
    background: linear-gradient(180deg, var(--header-mid) 0%, var(--header-light) 35%, var(--header-deep) 100%);
  }

  .status-bar {
    position: absolute; left: 0; top: 0; width: 675px; height: 40px;
    color: var(--white); font-family: 'Lato', sans-serif; font-size: 19px;
  }
  .status-bar .carrier { position: absolute; left: 12px; top: 10px; display: flex; align-items: center; gap: 6px; }
  .status-bar .time { position: absolute; left: 0; width: 675px; top: 10px; text-align: center; font-weight: 700; }
  .status-bar .battery-group { position: absolute; right: 12px; top: 10px; display: flex; align-items: center; gap: 8px; }

  .brand {
    position: absolute; left: 0; top: 100px; width: 675px; text-align: center;
    display: flex; justify-content: center; align-items: center; gap: 14px;
  }
  .brand-dot { width: 30px; height: 30px; border-radius: 50%; background: var(--white); }
  .brand-name { font-family: 'Lato', sans-serif; font-weight: 700; font-size: 58px; color: var(--white); letter-spacing: -0.5px; }

  .search {
    position: absolute; left: 50px; top: 207px; width: 570px; height: 56px;
    background: var(--search-bg); border-radius: 6px;
    display: flex; align-items: center; padding-left: 14px; gap: 12px;
    font-family: 'Lato', sans-serif; font-weight: 300; font-size: 23px; color: var(--search-text);
  }

  .category {
    position: absolute; width: 269px; height: 217px; background: var(--white);
    box-shadow: 0 2px 8px rgba(0,0,0,0.13);
    display: flex; flex-direction: column; align-items: center;
  }
  .category svg { position: absolute; fill: var(--brand-blue); }
  .category .label { position: absolute; left: 0; width: 100%; text-align: center; font-weight: 700; font-size: 19px; color: var(--label); }

  .bottom-nav { position: absolute; left: 4px; top: 1097px; width: 671px; height: 103px; border-top: 1px solid var(--divider); }
  .nav-icon { position: absolute; top: 32px; fill: none; stroke: var(--nav-icon); stroke-width: 2.2; }
  .fab {
    position: absolute; left: 289px; top: 1080px; width: 108px; height: 108px; border-radius: 50%;
    background: linear-gradient(180deg, var(--fab-top), var(--fab-bottom));
    box-shadow: 0 6px 14px rgba(220,30,60,0.3);
    display: flex; align-items: center; justify-content: center;
  }
</style>
</head>
<body>
<div class="screen">
  <div class="hero" role="img" aria-label="Blue-tinted photo of a waterfront city skyline with domes, minarets and seagulls"></div>

  <div class="status-bar">
    <div class="carrier">
      <svg width="56" height="12" viewBox="0 0 56 12" aria-hidden="true">
        <g fill="#fff"><circle cx="5" cy="6" r="4.5"/><circle cx="16" cy="6" r="4.5"/><circle cx="27" cy="6" r="4.5"/></g>
        <g fill="none" stroke="#fff" stroke-width="1.2"><circle cx="38" cy="6" r="4"/><circle cx="49" cy="6" r="4"/></g>
      </svg>
      <span>KESTREL</span>
      <svg width="20" height="15" viewBox="0 0 20 15" aria-hidden="true" fill="#fff">
        <path d="M10 15l3-3.6a4.5 4.5 0 0 0-6 0z"/>
        <path d="M10 6a8 8 0 0 1 5.6 2.3l-1.5 1.8a5.8 5.8 0 0 0-8.2 0L4.4 8.3A8 8 0 0 1 10 6z"/>
        <path d="M10 1a13 13 0 0 1 9.2 3.8l-1.5 1.8a10.8 10.8 0 0 0-15.4 0L.8 4.8A13 13 0 0 1 10 1z"/>
      </svg>
    </div>
    <div class="time">4:21 PM</div>
    <div class="battery-group">
      <svg width="12" height="20" viewBox="0 0 12 20" aria-hidden="true" fill="none" stroke="#9ec3f2" stroke-width="1.6">
        <path d="M1 6l10 8-5 4V2l5 4L1 14"/>
      </svg>
      <span>22%</span>
      <svg width="44" height="20" viewBox="0 0 44 20" aria-hidden="true">
        <rect x="1" y="2" width="38" height="16" rx="3" fill="none" stroke="#fff" stroke-width="1.5"/>
        <rect x="3.5" y="4.5" width="7" height="11" rx="1" fill="#fff"/>
        <rect x="40.5" y="7" width="2.5" height="6" rx="1" fill="#fff"/>
      </svg>
    </div>
  </div>

  <div class="brand">
    <span class="brand-dot" aria-hidden="true"></span>
    <span class="brand-name">Merrows</span>
  </div>

  <div class="search">
    <svg width="26" height="26" viewBox="0 0 26 26" aria-hidden="true" fill="none" stroke="#8c8c8c" stroke-width="2">
      <circle cx="10.5" cy="10.5" r="8"/><path d="M16.5 16.5l7 7"/>
    </svg>
    <span>Search</span>
  </div>

  <!-- Accommodations -->
  <div class="category" style="left:50px; top:325px;">
    <svg style="left:96px; top:50px;" width="76" height="64" viewBox="0 0 76 64" aria-hidden="true">
      <path d="M38 0L0 34h11v30h22V46h10v18h22V34h11L61 14V2h-8v5z"/>
    </svg>
    <div class="label" style="top:137px;">Accomodations</div>
  </div>

  <!-- Transportation -->
  <div class="category" style="left:351px; top:325px;">
    <svg style="left:96px; top:56px;" width="76" height="56" viewBox="0 0 76 56" aria-hidden="true">
      <path d="M16 2h44c3 0 5 2 6 4l6 16h3v4h-2v20h-12v6a3 3 0 0 1-3 3h-6a3 3 0 0 1-3-3v-6H27v6a3 3 0 0 1-3 3h-6a3 3 0 0 1-3-3v-6H4V26H1v-4h4l5-16c1-2 3-4 6-4zm2 8l-4 12h48l-4-12zM14 38a5 5 0 1 0 10 0a5 5 0 1 0-10 0zm38 0a5 5 0 1 0 10 0a5 5 0 1 0-10 0z" fill-rule="evenodd"/>
    </svg>
    <div class="label" style="top:138px;">Transportation</div>
  </div>

  <!-- Food / Recipes -->
  <div class="category" style="left:50px; top:575px;">
    <svg style="left:96px; top:46px;" width="78" height="78" viewBox="0 0 24 24" aria-hidden="true">
      <path d="M8.1 13.34l2.83-2.83L3.91 3.5c-1.56 1.56-1.56 4.09 0 5.66l4.19 4.18zm6.78-1.81c1.53.71 3.68.21 5.27-1.38 1.91-1.91 2.28-4.65.81-6.12-1.46-1.46-4.2-1.1-6.12.81-1.59 1.59-2.09 3.74-1.38 5.27L3.7 19.87l1.41 1.41L12 14.41l6.88 6.88 1.41-1.41L13.41 13l1.47-1.47z"/>
    </svg>
    <div class="label" style="top:148px;">Food/Recipies</div>
  </div>

  <!-- Tour & Activities -->
  <div class="category" style="left:351px; top:575px;">
    <svg style="left:94px; top:48px;" width="82" height="82" viewBox="0 0 82 82" aria-hidden="true">
      <rect x="12" y="0" width="5" height="12" rx="2"/>
      <rect x="50" y="0" width="5" height="12" rx="2"/>
      <path d="M4 6h64v38h-5V22H9v40h30v5H4z"/>
      <g>
        <rect x="15" y="28" width="9" height="8"/><rect x="28" y="28" width="9" height="8"/><rect x="41" y="28" width="9" height="8"/><rect x="54" y="28" width="6" height="8"/>
        <rect x="15" y="40" width="9" height="8"/><rect x="28" y="40" width="9" height="8"/><rect x="41" y="40" width="6" height="6"/>
        <rect x="15" y="52" width="9" height="8"/><rect x="28" y="52" width="9" height="8"/>
      </g>
      <circle cx="61" cy="61" r="20"/>
      <circle cx="61" cy="61" r="15" fill="#fff"/>
      <path d="M59 51h4v10h8v4H59z"/>
    </svg>
    <div class="label" style="top:153px;">Tour &amp; Activities</div>
  </div>

  <!-- Hotel -->
  <div class="category" style="left:50px; top:822px;">
    <svg style="left:93px; top:39px;" width="84" height="83" viewBox="0 0 84 83" aria-hidden="true">
      <rect x="40" y="0" width="4" height="8"/>
      <path d="M28 8h28v75H47v-8a5 5 0 0 0-10 0v8h-9z"/>
      <rect x="0" y="38" width="24" height="45"/>
      <rect x="60" y="38" width="24" height="45"/>
      <g fill="#fff">
        <rect x="32" y="14" width="5" height="5"/><rect x="40" y="14" width="5" height="5"/><rect x="48" y="14" width="5" height="5"/>
        <rect x="32" y="24" width="5" height="5"/><rect x="40" y="24" width="5" height="5"/><rect x="48" y="24" width="5" height="5"/>
        <rect x="32" y="34" width="5" height="5"/><rect x="40" y="34" width="5" height="5"/><rect x="48" y="34" width="5" height="5"/>
        <rect x="32" y="44" width="5" height="5"/><rect x="40" y="44" width="5" height="5"/><rect x="48" y="44" width="5" height="5"/>
        <rect x="32" y="54" width="5" height="5"/><rect x="40" y="54" width="5" height="5"/><rect x="48" y="54" width="5" height="5"/>
        <rect x="30" y="64" width="24" height="3"/>
      </g>
    </svg>
    <div class="label" style="top:160px;">Hotel</div>
  </div>

  <!-- Flight -->
  <div class="category" style="left:351px; top:822px;">
    <svg style="left:90px; top:38px;" width="88" height="88" viewBox="0 0 24 24" aria-hidden="true">
      <path transform="rotate(45 12 12)" d="M21 16v-2l-8-5V3.5c0-.83-.67-1.5-1.5-1.5S10 2.67 10 3.5V9l-8 5v2l8-2.5V19l-2 1.5V22l3.5-1 3.5 1v-1.5L13 19v-5.5l8 2.5z"/>
    </svg>
    <div class="label" style="top:160px;">Flight</div>
  </div>

  <nav class="bottom-nav" aria-label="Main">
    <svg class="nav-icon" style="left:67px;" width="38" height="38" viewBox="0 0 38 38" aria-hidden="true">
      <path d="M4 4h30v24H12l-8 7z" stroke-linejoin="round"/>
      <path d="M10 12h18M10 17h18M10 22h12"/>
    </svg>
    <svg class="nav-icon" style="left:187px;" width="44" height="38" viewBox="0 0 44 38" aria-hidden="true">
      <circle cx="14" cy="12" r="6"/><circle cx="30" cy="12" r="6"/>
      <path d="M3 30c0-6 5-9 11-9s11 3 11 9zM25 22c1.5-.7 3.2-1 5-1 6 0 11 3 11 9H25"/>
    </svg>
    <svg class="nav-icon" style="left:447px;" width="40" height="38" viewBox="0 0 40 38" aria-hidden="true">
      <g fill="var(--nav-icon)" stroke="none"><circle cx="5" cy="9" r="2.4"/><circle cx="5" cy="19" r="2.4"/><circle cx="5" cy="29" r="2.4"/></g>
      <path d="M12 9h26M12 19h26M12 29h26" stroke-width="2.6"/>
    </svg>
    <svg class="nav-icon" style="left:573px;" width="38" height="38" viewBox="0 0 38 38" aria-hidden="true">
      <circle cx="19" cy="11" r="7"/>
      <path d="M5 33v-3c0-5 6-8 14-8s14 3 14 8v3z"/>
    </svg>
  </nav>

  <div class="fab" aria-label="Add">
    <svg width="28" height="28" viewBox="0 0 28 28" aria-hidden="true" fill="#fff">
      <rect x="12.5" y="0" width="3" height="28"/><rect x="0" y="12.5" width="28" height="3"/>
    </svg>
  </div>
</div>
</body>
</html>
```